vehicle livery flyer

a flyer to go under windscreen wipers solely aimed at van drivers / companies using the vans for advertising thier companies.... ie Van Livery

use company logo , file supplied and be creative

id like this re designed, using different pictures , same logo....in a postcard style.

Livery

```html
<!DOCTYPE html>
<html lang="en">
<head>
<meta charset="utf-8">
<title>Vantex Ltd – Vehicle Livery Flyer</title>
<link rel="stylesheet" href="https://fonts.googleapis.com/css2?family=Oswald:wght@400;500&family=Roboto+Condensed:ital,wght@1,700&family=Francois+One&display=swap">
<style>
  :root{
    --page:#e9e6e2;
    --ink:#0c0c12;
    --panel-navy:#0b0f2e;
    --panel-dark:#07070d;
    --steel:#2a2a30;
    --light:#f2f2f2;
    --light-shade:#cfcfcf;
    --purple:#7a1fd6;
    --purple-bright:#a23bff;
    --sky:#1e9be6;
    --yellow:#ffd21a;
    --white:#ffffff;
    --orange:#f29b12;
    --orange-deep:#d66f00;
  }
  *{margin:0;padding:0;box-sizing:border-box}
  html,body{width:1200px;height:1135px;overflow:hidden;background:var(--page)}
  .canvas{position:relative;width:1200px;height:1135px}
  .flyer{
    position:absolute;left:209px;top:25px;width:692px;height:959px;
    transform:scale(1.13);transform-origin:0 0;
    background:var(--ink);overflow:hidden;
    box-shadow:0 6px 24px rgba(0,0,0,.35);
  }
  .backdrop{position:absolute;inset:0;width:692px;height:959px}
  .brand{
    position:absolute;left:70px;top:60px;display:flex;align-items:center;gap:10px;
    font-family:"Oswald",sans-serif;font-weight:500;font-size:24px;color:var(--purple);
    z-index:2;white-space:nowrap;
  }
  .brand-dot{width:46px;height:46px;border-radius:50%;background:var(--sky)}
  .vehicle-photo{
    position:absolute;left:255px;top:22px;width:420px;height:228px;border-radius:40px;
    background:radial-gradient(ellipse at 35% 65%,#8fc13a 0%,#4a6b22 35%,rgba(40,40,50,.85) 60%,rgba(230,230,230,0) 78%);
  }
  .headline{
    position:absolute;left:202px;top:318px;transform:rotate(-5deg);transform-origin:0 0;
    font-family:"Francois One",sans-serif;font-weight:400;font-size:29px;color:var(--yellow);
    letter-spacing:-.6px;white-space:nowrap;
    text-shadow:1px 2px 0 rgba(0,0,0,.35);
  }
  .services{
    position:absolute;top:428px;list-style:none;
    font-family:"Oswald",sans-serif;font-weight:400;font-size:24px;color:var(--white);
  }
  .services li{height:35px;line-height:30px;position:relative}
  .services-left{left:80px}
  .services-right{right:86px;text-align:right}
  .services li::before{
    content:"";position:absolute;top:15px;height:2px;width:58px;background:var(--purple-bright);
  }
  .services li::after{
    content:"";position:absolute;top:11px;width:10px;height:10px;border-radius:50%;background:var(--purple-bright);
  }
  .services-left li::before{left:-80px}
  .services-left li::after{left:-26px}
  .services-right li::before{right:-84px}
  .services-right li::after{right:-28px}
  .call{position:absolute;left:75px;top:580px;font-family:"Roboto Condensed",sans-serif;font-style:italic;font-weight:700}
  .call-lead{font-size:33px;color:var(--purple-bright);line-height:36px}
  .call-tel{font-size:38px;color:var(--white);line-height:44px;letter-spacing:.5px}
  .phone-icon{position:absolute;left:10px;top:600px;width:50px;height:50px}
  .badge{position:absolute;left:450px;top:578px;width:118px;height:118px}
  .badge-text{
    position:absolute;left:456px;top:612px;width:106px;text-align:center;transform:rotate(-10deg);
    font-family:"Roboto Condensed",sans-serif;font-weight:700;font-style:italic;font-size:15px;line-height:17px;color:#3a1a00;
  }
  .gallery{position:absolute;top:704px;left:12px;display:flex;gap:8px}
  .gallery-item{height:116px;border:3px solid var(--white)}
  .shot-banner{width:160px;background:linear-gradient(135deg,#5b6b3a,#e0641e 60%,#2a2a2a)}
  .shot-stands{width:160px;background:linear-gradient(135deg,#f4f4f4,#c9b7a8 50%,#3b3b4a)}
  .shot-interior{width:150px;background:linear-gradient(135deg,#6b6e70,#b3a69c 55%,#4b4c4e)}
  .shot-glass{width:176px;background:linear-gradient(135deg,#c9c4c0,#e7e0ea 50%,#8aa7c4)}
  .contact{
    position:absolute;left:0;top:862px;width:465px;height:97px;background:var(--purple);
    font-family:"Oswald",sans-serif;font-size:20px;color:var(--white);padding:14px 0 0 44px;
  }
  .contact p{display:flex;align-items:center;gap:14px;height:33px;white-space:nowrap}
  .contact svg{width:26px;height:22px;flex:none}
  .social{position:absolute;left:480px;top:862px;width:200px;font-family:"Oswald",sans-serif;font-size:18px;color:var(--white)}
  .social-title{display:flex;align-items:center;gap:6px}
  .social-title::after{content:"";flex:1;height:2px;background:var(--purple);margin-top:6px}
  .social-links{display:flex;gap:16px;margin-top:8px}
  .social-links span{width:54px;height:54px;border-radius:4px;background:linear-gradient(180deg,#fafafa,#a9a9a9);box-shadow:0 1px 3px rgba(0,0,0,.5)}
</style>
</head>
<body>
<div class="canvas">
  <article class="flyer">
    <svg class="backdrop" viewBox="0 0 692 959" aria-hidden="true">
      <defs>
        <linearGradient id="lightGrad" x1="0" y1="0" x2="0" y2="1">
          <stop offset="0" stop-color="#fdfdfd"/><stop offset="1" stop-color="#d4d4d4"/>
        </linearGradient>
        <linearGradient id="steelGrad" x1="0" y1="0" x2="1" y2="1">
          <stop offset="0" stop-color="#3a3a40"/><stop offset="1" stop-color="#141418"/>
        </linearGradient>
        <linearGradient id="navyGrad" x1="0" y1="0" x2="1" y2="0">
          <stop offset="0" stop-color="#0a0d38"/><stop offset="1" stop-color="#070a22"/>
        </linearGradient>
        <radialGradient id="badgeGrad" cx=".45" cy=".4" r=".6">
          <stop offset="0" stop-color="#ffc04a"/><stop offset="1" stop-color="#e27d00"/>
        </radialGradient>
      </defs>
      <rect width="692" height="959" fill="#0a0a10"/>
      <polygon points="0,0 155,272 212,392 0,402" fill="url(#steelGrad)"/>
      <polygon points="0,560 692,560 692,700 0,700" fill="#121216"/>
      <polygon points="0,402 310,402 310,572 0,572" fill="url(#navyGrad)"/>
      <polygon points="310,330 692,320 692,572 310,572" fill="#06060c"/>
      <polygon points="4,0 692,0 692,258 155,272" fill="url(#lightGrad)"/>
      <polygon points="155,272 692,258 692,285 168,298" fill="var(--purple)"/>
      <polygon points="168,298 692,285 692,332 200,376" fill="var(--sky)"/>
      <polygon points="200,376 692,332 692,340 206,392" fill="#e8e8e8"/>
      <polygon points="0,700 692,700 692,959 0,959" fill="#0c0c0f"/>
    </svg>

    <div class="vehicle-photo" role="img" aria-label="Photo of a small car and a van wrapped in full colour advertising livery"></div>

    <div class="brand"><span class="brand-dot"></span>Vantex Ltd</div>

    <h1 class="headline">The Latest In Digital Print Technology</h1>

    <ul class="services services-left">
      <li>BANNERS</li><li>EXHIBITIONS</li><li>EXTERIOR SIGNAGE</li><li>GLASS PRINTING</li>
    </ul>
    <ul class="services services-right">
      <li>INTERIOR GRAPHICS</li><li>POSTERS</li><li>RETAIL GRAPHICS</li><li>VEHICLE GRAPHICS</li>
    </ul>

    <svg class="phone-icon" viewBox="0 0 50 50" aria-hidden="true">
      <path d="M14 8c3 0 5 6 5 8s-4 3-4 5 6 11 9 12 3-3 5-3 7 3 7 6-4 7-8 7C18 45 5 30 5 18c0-5 5-10 9-10z" fill="#9a9aa2"/>
      <path d="M30 6a14 14 0 0 1 14 14M30 13a7 7 0 0 1 7 7" stroke="#9a9aa2" stroke-width="3" fill="none"/>
    </svg>
    <div class="call">
      <p class="call-lead">Call Now...</p>
      <p class="call-tel">Tel: 020 7946 0318</p>
    </div>

    <svg class="badge" viewBox="0 0 118 118" aria-hidden="true">
      <circle cx="59" cy="59" r="56" fill="#c9c9c9"/>
      <circle cx="59" cy="59" r="50" fill="url(#badgeGrad)" stroke="#fff" stroke-width="2" stroke-dasharray="3 3"/>
    </svg>
    <p class="badge-text">Come &amp; see<br>the difference</p>

    <div class="gallery">
      <div class="gallery-item shot-banner" role="img" aria-label="Photo of an outdoor sale banner on a roadside fence"></div>
      <div class="gallery-item shot-stands" role="img" aria-label="Photo of printed exhibition roller stands"></div>
      <div class="gallery-item shot-interior" role="img" aria-label="Photo of interior wall graphics in a shop"></div>
      <div class="gallery-item shot-glass" role="img" aria-label="Photo of printed frosted glass office partitions"></div>
    </div>

    <footer class="contact">
      <p><svg viewBox="0 0 26 22" aria-hidden="true"><circle cx="13" cy="11" r="9" fill="none" stroke="#cbb7ff" stroke-width="2"/><path d="M13 11l5-5" stroke="#cbb7ff" stroke-width="2"/></svg>14 Halden Road, Croydon, Surrey, CR0 2XT.</p>
      <p><svg viewBox="0 0 26 22" aria-hidden="true"><rect x="2" y="4" width="22" height="14" fill="none" stroke="#cbb7ff" stroke-width="2"/><path d="M2 4l11 8 11-8" fill="none" stroke="#cbb7ff" stroke-width="2"/></svg>hello@vantex-ltd.com</p>
    </footer>

    <div class="social">
      <p class="social-title">Find Us on</p>
      <div class="social-links"><span></span><span></span><span></span></div>
    </div>
  </article>
</div>
</body>
</html>
```